Velmora Education General Flyer Design

Updates
Reason: We are very close to making a selection but would like to provide a little more time for some of the designers to complete their revisions.
Target Market(s)
Secondary school students
Industry/Entity Type
Education
Requirements
Must have
- company logo and company name (see attached file)

```html
<!DOCTYPE html>
<html lang="en">
<head>
<meta charset="UTF-8">
<title>Velmora Education – Exam Preparation</title>
<link href="https://fonts.googleapis.com/css2?family=Open+Sans:ital,wght@0,700;0,800;1,600;1,700&family=Roboto+Condensed:ital,wght@0,400;1,400;1,700&display=swap" rel="stylesheet">
<style>
  :root {
    --red: #c8141e;
    --red-deep: #8a0d12;
    --cream: #fdf1cc;
    --cream-light: #fffaf0;
    --peach: #fbd48a;
    --orange: #f29a2e;
    --ink: #111111;
    --yellow: #ffd21f;
    --white: #ffffff;
  }
  * { box-sizing: border-box; margin: 0; padding: 0; }
  html, body { width: 776px; height: 1200px; overflow: hidden; background: var(--white); }
  .flyer { position: relative; width: 776px; height: 1200px; overflow: hidden; font-family: "Open Sans", Arial, sans-serif; }

  .title-band {
    position: absolute; left: 0; top: 0; width: 776px; height: 122px;
    background: linear-gradient(90deg, var(--red) 0%, #b0121a 60%, var(--red-deep) 100%);
    display: flex; align-items: center; justify-content: center;
  }
  .title-band h1 { color: var(--white); font-weight: 800; font-size: 50px; letter-spacing: 1px; }

  .slogan-band {
    position: absolute; left: 0; top: 122px; width: 776px; height: 202px;
    background: linear-gradient(180deg, var(--cream) 0%, var(--cream-light) 100%);
    display: flex; flex-direction: column; align-items: center; justify-content: center;
  }
  .slogan-band p {
    color: var(--red); font-style: italic; font-weight: 700; font-size: 33px;
    line-height: 44px; text-transform: uppercase; letter-spacing: 1px;
  }

  .hero-photo {
    position: absolute; left: 0; top: 324px; width: 776px; height: 452px;
    background: radial-gradient(ellipse at 55% 70%, #c9d6de 0%, #7f8f8a 45%, #4f5f58 100%);
  }
  .divider { position: absolute; left: 0; top: 776px; width: 776px; height: 4px; background: var(--red); }

  .brand-panel {
    position: absolute; left: 0; top: 780px; width: 374px; height: 222px;
    background: linear-gradient(180deg, var(--cream-light) 0%, var(--cream) 100%);
    display: flex; flex-direction: column; align-items: center; justify-content: center;
  }
  .brand-mark { width: 70px; height: 70px; background: var(--red-deep); margin-bottom: 18px; }
  .brand-name { font-weight: 700; font-size: 30px; color: var(--ink); }
  .brand-tagline { font-style: italic; font-weight: 600; font-size: 22px; color: var(--red); margin-top: 2px; }

  .exams-panel {
    position: absolute; left: 374px; top: 780px; width: 402px; height: 230px;
    background: linear-gradient(180deg, #f4f4f4 0%, var(--white) 100%);
    padding: 44px 0 0 90px;
  }
  .exams-panel h2 {
    font-family: "Roboto Condensed", Arial Narrow, sans-serif; font-style: italic; font-weight: 400;
    color: var(--red); font-size: 31px; margin-bottom: 8px;
  }
  .exams-list { list-style: none; padding-left: 34px; }
  .exams-list li { font-size: 19px; line-height: 32px; color: var(--ink); font-family: Arial, sans-serif; }

  .contact-panel {
    position: absolute; left: 0; top: 1002px; width: 374px; height: 198px;
    background: linear-gradient(180deg, var(--peach) 0%, var(--orange) 100%);
    padding: 28px 0 0 38px;
    font-family: "Roboto Condensed", Arial Narrow, sans-serif; color: var(--ink); font-size: 17px; line-height: 24px;
  }
  .contact-panel h3 { font-style: italic; font-weight: 400; color: var(--red); font-size: 20px; line-height: 26px; }

  .promo-panel {
    position: absolute; left: 374px; top: 1010px; width: 402px; height: 190px;
    background: linear-gradient(90deg, var(--red) 0%, var(--red-deep) 100%);
    display: flex; flex-direction: column; align-items: center; justify-content: center;
    font-family: "Roboto Condensed", Arial Narrow, sans-serif; font-style: italic; text-transform: uppercase; text-align: center;
  }
  .promo-label { color: var(--yellow); font-size: 20px; line-height: 28px; }
  .promo-headline { color: var(--white); font-size: 31px; line-height: 38px; }
  .promo-note { color: var(--white); font-size: 18px; line-height: 26px; }
  .promo-call { color: var(--yellow); font-size: 27px; line-height: 34px; }
</style>
</head>
<body>
<div class="flyer">
  <header class="title-band"><h1>EXAM PREPARATION</h1></header>

  <section class="slogan-band">
    <p>Come out on top.</p>
    <p>We can help.</p>
    <p>Score!</p>
    <p>With our help.</p>
  </section>

  <div class="hero-photo" role="img" aria-label="Student seen from behind, scratching his head in front of a chalkboard full of maths equations"></div>
  <div class="divider"></div>

  <section class="brand-panel">
    <div class="brand-mark"></div>
    <div class="brand-name">Velmora Education</div>
    <div class="brand-tagline">Your Pathway to Excellence</div>
  </section>

  <section class="exams-panel">
    <h2>EXAMS WE COVER:</h2>
    <ol class="exams-list">
      <li>1) SAT</li>
      <li>2) PSAT</li>
      <li>3) SSAT</li>
      <li>4) OSSLT</li>
    </ol>
  </section>

  <section class="contact-panel">
    <h3>CONTACT:</h3>
    <p>Address: 1470 Larkspur Avenue, Unit 305</p>
    <p>Ashford, ON K7T 2M9</p>
    <p>Email: Hello@VelmoraEducation.com</p>
    <p>Tel: 555-204-7186</p>
    <p>Website: www.VelmoraEducation.com</p>
  </section>

  <section class="promo-panel">
    <p class="promo-label">Promotional offer:</p>
    <p class="promo-headline">Free trial lesson</p>
    <p class="promo-note">Try us out before you enroll!</p>
    <p class="promo-call">Call or email</p>
    <p class="promo-note">Us today for a free trial lesson!</p>
  </section>
</div>
</body>
</html>
```